School Management website

I need page design for our school management system website

Base website is www.brivalo.com. When the student logs in, he will reach the below pages.
You can either design with white and blue background or grey and white background

Page 1 - School Info

Header
product name("Brivalo") in left corner
logout link in right corner

LeftMenu

Dashboard
School Info
School Settings
Staffs
Classes
Messaging
Contact Us

Footer
About link and copyright text

School Info content
The page should have breadcrumb

The content of this page will be the school profile
We have to show the school logo
Name
School Type
School Code
School Count
School Address
School phone 1&2
School Email
School Website

The page content should show edit school profile link which will take the user to another page

Industry/Entity Type

School

```html
<!DOCTYPE html>
<html lang="en">
<head>
<meta charset="utf-8">
<title>Brivalo – School Info</title>
<link href="https://fonts.googleapis.com/css2?family=Roboto+Condensed:wght@400;700&display=swap" rel="stylesheet">
<style>
:root{
  --blue-dark:#0f5f94;
  --blue:#0b6aa8;
  --accent:#29a9e1;
  --white:#ffffff;
  --ink:#333333;
  --muted:#8a8a8a;
  --row:#f5f5f5;
  --line:#d9d9d9;
  --crumb-top:#4a4546;
  --crumb-bot:#2f2b2c;
  --footer:#1f1f1f;
  --btn:#666666;
}
*{margin:0;padding:0;box-sizing:border-box}
html,body{width:1200px;height:839px;overflow:hidden}
body{position:relative;font-family:"Roboto Condensed",Arial,sans-serif;background:var(--blue)}
.site-header{position:absolute;left:0;top:0;width:1200px;height:57px;background:linear-gradient(#ffffff,#ececec);border-bottom:1px solid #c9c9c9}
.brand{position:absolute;left:42px;top:10px;font-size:34px;font-weight:700;color:#7d7d7d;letter-spacing:.5px}
.logout{position:absolute;left:1080px;top:17px;width:83px;height:29px;border-radius:15px;background:linear-gradient(#4fbcec,#1a8fcf);border:2px solid #1683c0;color:var(--white);font-size:13px;font-weight:700;display:flex;align-items:center;padding-left:30px;text-decoration:none}
.logout svg{position:absolute;left:2px;top:1px}
.main{position:absolute;left:0;top:57px;width:1200px;height:731px;background:linear-gradient(var(--blue-dark),var(--blue));border-left:1px solid #0a4a74}
.side-nav{position:absolute;left:33px;top:0;width:202px}
.nav-item{position:absolute;left:0;height:46px;width:202px;display:flex;align-items:center;padding-left:46px;color:var(--white);font-size:15px;text-transform:uppercase;text-decoration:none}
.nav-item svg{position:absolute;left:7px;top:10px}
.nav-item.dashboard{font-size:17px}
.nav-item.active{background:var(--white);color:var(--blue);border-radius:8px 0 0 8px}
.breadcrumb{position:absolute;left:236px;top:33px;width:917px;height:34px;border-radius:7px;background:linear-gradient(var(--crumb-top),var(--crumb-bot));color:var(--white);font-size:13px}
.breadcrumb span{position:absolute;top:10px}
.panel{position:absolute;left:235px;top:73px;width:919px;height:650px;background:var(--white);border-radius:8px}
.school-mark{position:absolute;left:65px;top:44px;display:flex;align-items:center;gap:8px;font-size:30px;font-weight:700;color:var(--muted)}
.school-mark i{display:block;width:14px;height:14px;background:var(--accent)}
.edit-btn{position:absolute;left:827px;top:58px;width:59px;height:28px;border-radius:6px;background:var(--btn);color:var(--white);font-weight:700;font-size:16px;display:flex;align-items:center;justify-content:center;text-decoration:none}
.profile{position:absolute;left:25px;top:105px;width:873px;border:1px solid var(--line);border-radius:6px;background:var(--row);overflow:hidden}
.profile .row{height:50px;display:flex;align-items:center;font-size:17px;color:var(--ink);border-top:2px solid #e2e2e2}
.profile .row:first-child{border-top:none}
.profile .label{width:191px;padding-left:42px;height:26px;line-height:26px;border-right:1px solid #cfcfcf}
.profile .value{padding-left:33px}
.site-footer{position:absolute;left:0;top:788px;width:1200px;height:51px;background:var(--footer);color:#bdbdbd;font-size:12px}
.site-footer p{position:absolute;right:60px;top:18px}
.site-footer a{color:var(--accent);text-decoration:none}
</style>
</head>
<body>
<header class="site-header">
  <div class="brand">Brivalo</div>
  <a class="logout" href="#">
    <svg width="24" height="24" viewBox="0 0 24 24"><circle cx="12" cy="12" r="11" fill="#1683c0"/><path d="M8.5 11V8.5a3.5 3.5 0 0 1 7 0V11" fill="none" stroke="#fff" stroke-width="2"/><rect x="7" y="11" width="10" height="8" rx="1.5" fill="#fff"/></svg>
    Logout
  </a>
</header>

<div class="main">
  <nav class="side-nav">
    <a class="nav-item dashboard" href="#" style="top:28px">
      <svg width="26" height="26" viewBox="0 0 26 26"><circle cx="13" cy="13" r="11" fill="none" stroke="#29a9e1" stroke-width="2"/><path d="M13 13l5-5" stroke="#29a9e1" stroke-width="2"/><circle cx="13" cy="13" r="2" fill="#29a9e1"/></svg>
      Dashboard</a>
    <a class="nav-item active" href="#" style="top:102px">
      <svg width="26" height="26" viewBox="0 0 26 26"><circle cx="13" cy="13" r="11.5" fill="none" stroke="#555" stroke-width="1.5"/><circle cx="13" cy="8" r="1.6" fill="#555"/><rect x="11.6" y="11" width="2.8" height="8" fill="#555"/></svg>
      School Info</a>
    <a class="nav-item" href="#" style="top:152px">
      <svg width="26" height="26" viewBox="0 0 26 26"><circle cx="13" cy="13" r="9" fill="none" stroke="#fff" stroke-width="4" stroke-dasharray="4 3"/><circle cx="13" cy="13" r="6" fill="none" stroke="#fff" stroke-width="3"/></svg>
      School Settings</a>
    <a class="nav-item" href="#" style="top:202px">
      <svg width="28" height="26" viewBox="0 0 28 26"><circle cx="10" cy="7" r="5" fill="#fff"/><path d="M1 24c0-7 4-10 9-10s9 3 9 10z" fill="#fff"/><circle cx="21" cy="14" r="3.5" fill="#fff"/><path d="M15 25c0-5 3-7 6-7s6 2 6 7z" fill="#fff"/></svg>
      Staffs</a>
    <a class="nav-item" href="#" style="top:252px">
      <svg width="28" height="28" viewBox="0 0 28 28"><rect x="9" y="2" width="17" height="13" fill="none" stroke="#fff" stroke-width="2"/><circle cx="5" cy="5" r="3" fill="#fff"/><rect x="2" y="9" width="6" height="17" fill="#fff"/><path d="M17 15v6M13 24l4-3 4 3" stroke="#fff" stroke-width="1.5" fill="none"/></svg>
      Classes</a>
    <a class="nav-item" href="#" style="top:302px">
      <svg width="28" height="24" viewBox="0 0 28 24"><ellipse cx="11" cy="9" rx="10" ry="7" fill="#fff"/><ellipse cx="18" cy="14" rx="9" ry="6.5" fill="#fff" stroke="#0d65a0" stroke-width="1.5"/></svg>
      Messaging</a>
    <a class="nav-item" href="#" style="top:352px">
      <svg width="28" height="28" viewBox="0 0 28 28"><circle cx="14" cy="14" r="12.5" fill="none" stroke="#fff" stroke-width="2"/><path d="M10 7c-2 1-2 4 0 8s5 7 8 7c1 0 2-1 2-2l-3-3-2 1c-2-1-3-3-4-5l1-2-2-4z" fill="#fff"/></svg>
      Contact Us</a>
  </nav>

  <div class="breadcrumb">
    <svg style="position:absolute;left:13px;top:9px" width="20" height="16" viewBox="0 0 20 16"><path d="M10 1L1 9h3v6h4v-4h4v4h4V9h3z" fill="#bdbdbd"/></svg>
    <svg style="position:absolute;left:46px;top:0" width="10" height="34" viewBox="0 0 10 34"><path d="M1 0l7 17-7 17" fill="none" stroke="#888" stroke-width="1.5"/></svg>
    <span style="left:69px">DASHBOARD</span>
    <svg style="position:absolute;left:151px;top:0" width="10" height="34" viewBox="0 0 10 34"><path d="M1 0l7 17-7 17" fill="none" stroke="#888" stroke-width="1.5"/></svg>
    <span style="left:177px">SCHOOL INFO</span>
    <svg style="position:absolute;left:262px;top:0" width="10" height="34" viewBox="0 0 10 34"><path d="M1 0l7 17-7 17" fill="none" stroke="#888" stroke-width="1.5"/></svg>
  </div>

  <section class="panel">
    <div class="school-mark"><i></i>Brivalo</div>
    <a class="edit-btn" href="#">Edit</a>
    <div class="profile">
      <div class="row"><div class="label">Name</div><div class="value">ABC</div></div>
      <div class="row"><div class="label">School Type</div><div class="value">ABC</div></div>
      <div class="row"><div class="label">School Code</div><div class="value">1023654</div></div>
      <div class="row"><div class="label">School Count</div><div class="value">65897</div></div>
      <div class="row"><div class="label">School Address</div><div class="value">ABC, State, City, Country.</div></div>
      <div class="row"><div class="label">School Phone 1&amp;2</div><div class="value">091-4372-5810-27</div></div>
      <div class="row"><div class="label">School Email</div><div class="value">office@brivalo-mail.com</div></div>
      <div class="row"><div class="label">School Website</div><div class="value">www.brivalo.com</div></div>
    </div>
  </section>
</div>

<footer class="site-footer">
  <p><a href="#">About Us</a> / Copyright © 2014 &nbsp;|&nbsp; All Rights Reserved</p>
</footer>
</body>
</html>
```